small auto electrical company needs new logo and business cards !!!

we are a small auto electrical company (Velmor Autos Ltd) that has been running for 13 years the logo we have was put together by dinosaurs so we are looking at re branding the company starting with business cards and a new logo we fit GPS tracking devices for young drivers through there insurance company also we fit hands free systems and dash cameras also safety locks to fleet vehicles we would like bright eye catching colours day glow and neon and quirky designs for the logo our original logo was baby blue which i have added a picture enclosed we would like double sided but have a space to write notes and prices preferably not white on back same colour throughout many thanks
Reason: Just a chance to finalise any designs we want VA logos or V logos - No vlm's and no dinosaurs lol
Business
Installs@velmorautos.co.uk
07922483617
www.Velmorautos.co.uk
Velmor Autos Ltd - Fleets and Insurance Services
- new logo design !!
- Satellite in logo or something attaining to gps
- maybe a car in the logo
- shouldnt have velmor as vlm it is VeLMOR Autos

```html
<!DOCTYPE html>
<html lang="en">
<head>
<meta charset="utf-8">
<title>Velmor Autos Ltd – Business Card, Front and Back</title>
<link rel="stylesheet" href="https://fonts.googleapis.com/css2?family=PT+Sans:wght@400;700&display=swap">
<style>
  :root {
    --backdrop: #e4e4e4;
    --card: #ffffff;
    --brand-blue: #00a9ec;
    --faint: #eeeeee;
    --ink: #2b2b2b;
    --muted: #3a3a3a;
    --tagline: #555555;
  }
  html, body {
    margin: 0;
    width: 1200px;
    height: 900px;
    overflow: hidden;
    background: var(--backdrop);
    font-family: "PT Sans", Arial, sans-serif;
  }
  .business-card {
    position: absolute;
    left: 250px;
    width: 700px;
    height: 400px;
    background: var(--card);
    box-shadow: 0 4px 18px rgba(0,0,0,0.12);
    overflow: hidden;
  }
  .card-front { top: 35px; }
  .card-back  { top: 465px; }

  /* Front */
  .band-thin {
    position: absolute;
    left: 0;
    top: 100px;
    width: 290px;
    height: 18px;
    background: var(--brand-blue);
  }
  .band-wide {
    position: absolute;
    left: 290px;
    top: 116px;
    width: 410px;
    height: 42px;
    background: var(--brand-blue);
  }
  .brand-lockup {
    position: absolute;
    display: flex;
    align-items: center;
    gap: 10px;
  }
  .card-front .brand-lockup { left: 34px; top: 262px; }
  .brand-mark {
    flex: none;
    width: 20px;
    height: 20px;
    border-radius: 50%;
    background: var(--brand-blue);
  }
  .brand-text { display: flex; flex-direction: column; }
  .brand-name {
    font-weight: 700;
    font-size: 25px;
    line-height: 1;
    letter-spacing: 0.5px;
    text-transform: uppercase;
    color: var(--brand-blue);
  }
  .brand-tagline {
    margin-top: 4px;
    font-size: 11.5px;
    letter-spacing: 1.6px;
    text-transform: uppercase;
    color: var(--tagline);
  }
  .holder {
    position: absolute;
    left: 345px;
    top: 62px;
  }
  .holder-name {
    font-size: 24px;
    color: var(--brand-blue);
    line-height: 1;
  }
  .holder-role {
    font-size: 13px;
    color: var(--ink);
    margin-top: 3px;
  }
  .contact-list {
    position: absolute;
    left: 355px;
    top: 198px;
    margin: 0;
    padding: 0;
    list-style: none;
  }
  .contact-item {
    display: flex;
    align-items: flex-start;
    gap: 10px;
    font-size: 19px;
    color: var(--muted);
    line-height: 1.2;
    margin-bottom: 10px;
  }
  .contact-icon {
    flex: none;
    width: 17px;
    height: 17px;
    margin-top: 3px;
  }

  /* Back */
  .back-band {
    position: absolute;
    left: 0;
    top: 96px;
    width: 700px;
    height: 18px;
    background: var(--brand-blue);
  }
  .back-decor {
    position: absolute;
    left: 255px;
    top: 30px;
    width: 150px;
    height: 150px;
    border-radius: 50%;
    background: var(--faint);
  }
  .card-back .brand-lockup {
    left: 0;
    right: 0;
    top: 205px;
    justify-content: center;
  }
  .card-back .brand-name { font-size: 34px; }
  .card-back .brand-tagline { font-size: 15px; letter-spacing: 2.4px; }
</style>
</head>
<body>
  <div class="business-card card-front">
    <div class="band-thin"></div>
    <div class="band-wide"></div>

    <div class="brand-lockup">
      <span class="brand-mark"></span>
      <div class="brand-text">
        <span class="brand-name">Velmor Autos Ltd</span>
        <span class="brand-tagline">Fleet &amp; Insurance Services</span>
      </div>
    </div>

    <div class="holder">
      <div class="holder-name">Xxxxx Xxxxxx</div>
      <div class="holder-role">Director</div>
    </div>

    <ul class="contact-list">
      <li class="contact-item">
        <svg class="contact-icon" viewBox="0 0 26 26" aria-hidden="true">
          <circle cx="13" cy="13" r="13" fill="var(--brand-blue)"/>
          <rect x="6" y="8" width="14" height="10" fill="none" stroke="#fff" stroke-width="1.8"/>
          <path d="M6 8 L13 14 L20 8" fill="none" stroke="#fff" stroke-width="1.8"/>
        </svg>
        <span>Installs@velmorautos.co.uk</span>
      </li>
      <li class="contact-item">
        <svg class="contact-icon" viewBox="0 0 26 26" aria-hidden="true">
          <circle cx="13" cy="13" r="13" fill="var(--brand-blue)"/>
          <rect x="9" y="5.5" width="8" height="15" rx="1.5" fill="none" stroke="#fff" stroke-width="1.8"/>
          <circle cx="13" cy="17.5" r="1" fill="#fff"/>
        </svg>
        <span>07922483617</span>
      </li>
      <li class="contact-item">
        <svg class="contact-icon" viewBox="0 0 26 26" aria-hidden="true">
          <circle cx="13" cy="13" r="13" fill="var(--brand-blue)"/>
          <circle cx="13" cy="13" r="7" fill="none" stroke="#fff" stroke-width="1.6"/>
          <ellipse cx="13" cy="13" rx="3" ry="7" fill="none" stroke="#fff" stroke-width="1.4"/>
          <line x1="6" y1="13" x2="20" y2="13" stroke="#fff" stroke-width="1.4"/>
        </svg>
        <span>www.Velmorautos.co.uk</span>
      </li>
      <li class="contact-item">
        <svg class="contact-icon" viewBox="0 0 26 26" aria-hidden="true">
          <circle cx="13" cy="13" r="13" fill="var(--brand-blue)"/>
          <path d="M6 13 L13 6.5 L20 13 M8.5 11 V19 H17.5 V11" fill="none" stroke="#fff" stroke-width="1.8"/>
        </svg>
        <span>xxx xxxxx xxxxx xxx<br>xxxx</span>
      </li>
    </ul>
  </div>

  <div class="business-card card-back">
    <div class="back-decor"></div>
    <div class="back-band"></div>
    <div class="brand-lockup">
      <span class="brand-mark"></span>
      <div class="brand-text">
        <span class="brand-name">Velmor Autos Ltd</span>
        <span class="brand-tagline">Fleet &amp; Insurance Services</span>
      </div>
    </div>
  </div>
</body>
</html>
```